Bright Harbor Consulting

I need a business card design and for my consulting business. I provide outsourced CFO services for start-ups and high growth companies. I call my company Bright Harbor Co because building a company is similar to building a stone pathway, selecting each stone and planning several stones head in order to properly place them - all while keeping an eye on the final design and curve of the path. The underlying idea I want to express with my marketing images is that I'm someone that you can count on to help build your business and be there step by step to help. I'm not the old gray-haired CFO that many folks think of. :) I've included a one-page summery that I'm working on, it includes a summary of what I do. I've used a muted pathway and with greens in the header , and do like the green, but am open to other colors if they work well. Would like something that looks like a pathway, but a more abstract version instead of a picture.

```html
<!DOCTYPE html>
<html lang="en">
<head>
<meta charset="utf-8">
<title>Bright Harbor Co — Business Card</title>
<link href="https://fonts.googleapis.com/css2?family=Crimson+Text:wght@400;600&display=swap" rel="stylesheet">
<style>
  :root {
    --brand-green: #0b9444;
    --deep-green: #0a6b34;
    --ink: #1f2a24;
    --paper: #ffffff;
    --rule: #b9bdbb;
    --backdrop: #e6e7e6;
  }
  * { margin: 0; padding: 0; box-sizing: border-box; }
  html, body {
    width: 1200px; height: 900px; overflow: hidden;
    background: var(--backdrop);
    font-family: "Crimson Text", Georgia, serif;
  }
  .canvas {
    width: 1200px; height: 900px;
    display: flex; flex-direction: column; align-items: center; justify-content: center;
    gap: 40px;
  }
  .card {
    width: 700px; height: 400px;
    box-shadow: 0 6px 18px rgba(0,0,0,0.18);
    position: relative;
  }
  /* Front side */
  .card-front {
    background: var(--paper);
    display: grid;
    grid-template-columns: 1fr 1px 1fr;
    align-items: center;
    padding: 0 36px;
  }
  .brand-block { display: flex; flex-direction: column; align-items: center; text-align: center; }
  .brand-square {
    width: 120px; height: 110px; background: var(--brand-green); margin-bottom: 16px;
  }
  .brand-name {
    font-weight: 600; font-size: 28px; letter-spacing: 0.5px;
    color: var(--deep-green); text-transform: uppercase; line-height: 1;
  }
  .tagline {
    margin-top: 8px; font-size: 17px; line-height: 1.2; color: var(--deep-green);
  }
  .divider { width: 1px; height: 240px; background: var(--rule); }
  .contact-block { padding-left: 34px; }
  .person-name { font-size: 36px; font-weight: 400; color: var(--brand-green); line-height: 1; }
  .person-title { font-size: 19px; color: var(--ink); margin-bottom: 34px; }
  .contact-list { list-style: none; display: flex; flex-direction: column; gap: 12px; }
  .contact-item { display: flex; align-items: center; gap: 12px; font-size: 19px; color: var(--ink); }
  .contact-icon { width: 24px; height: 24px; flex: none; }
  /* Back side */
  .card-back {
    background: var(--brand-green);
    display: flex; align-items: center; justify-content: center;
  }
  .card-back .brand-square { background: var(--paper); width: 140px; height: 125px; }
  .card-back .brand-name { color: var(--paper); font-size: 32px; }
  .card-back .tagline { color: var(--paper); font-size: 19px; }
</style>
</head>
<body>
<main class="canvas">
  <section class="card card-front" aria-label="Card front">
    <div class="brand-block">
      <div class="brand-square" aria-hidden="true"></div>
      <div class="brand-name">Bright Harbor Co</div>
      <p class="tagline">Guiding Growing Companies<br>— Every Stage of the Way —</p>
    </div>
    <div class="divider" aria-hidden="true"></div>
    <div class="contact-block">
      <h1 class="person-name">Dana Whitfield</h1>
      <p class="person-title">CPA</p>
      <ul class="contact-list">
        <li class="contact-item">
          <svg class="contact-icon" viewBox="0 0 24 24" aria-hidden="true">
            <circle cx="12" cy="12" r="11" fill="none" stroke="#0b9444" stroke-width="1.5"/>
            <rect x="8.5" y="5.5" width="7" height="13" rx="1.2" fill="none" stroke="#0b9444" stroke-width="1.4"/>
            <line x1="10.5" y1="16.3" x2="13.5" y2="16.3" stroke="#0b9444" stroke-width="1.2"/>
          </svg>
          555-014-2277
        </li>
        <li class="contact-item">
          <svg class="contact-icon" viewBox="0 0 24 24" aria-hidden="true">
            <circle cx="12" cy="12" r="11" fill="none" stroke="#0b9444" stroke-width="1.5"/>
            <circle cx="12" cy="12" r="6.5" fill="none" stroke="#0b9444" stroke-width="1.2"/>
            <ellipse cx="12" cy="12" rx="2.8" ry="6.5" fill="none" stroke="#0b9444" stroke-width="1.1"/>
            <line x1="5.5" y1="12" x2="18.5" y2="12" stroke="#0b9444" stroke-width="1.1"/>
          </svg>
          www.brightharborco.com
        </li>
        <li class="contact-item">
          <svg class="contact-icon" viewBox="0 0 24 24" aria-hidden="true">
            <circle cx="12" cy="12" r="11" fill="none" stroke="#0b9444" stroke-width="1.5"/>
            <rect x="6" y="8" width="12" height="8.5" fill="none" stroke="#0b9444" stroke-width="1.3"/>
            <polyline points="6,8 12,13 18,8" fill="none" stroke="#0b9444" stroke-width="1.3"/>
          </svg>
          dana@brightharborco.com
        </li>
      </ul>
    </div>
  </section>

  <section class="card card-back" aria-label="Card back">
    <div class="brand-block">
      <div class="brand-square" aria-hidden="true"></div>
      <div class="brand-name">Bright Harbor Co</div>
      <p class="tagline">Guiding Growing Companies<br>— Every Stage of the Way —</p>
    </div>
  </section>
</main>
</body>
</html>
```